Business school needs a web design

Who We are:
KRVT is a small business school that offers programs in Project Management. The school is based in West Africa and welcomes students from the whole area. Our aim is to become one of the reference business schools in Africa.

Project Brief:
The site will include all informations relevant for different types of visitors that we have: actual and future students, companies, mass media, future employees, ect. It will present information about subscription, list of programs, presentation of the school and its team,etc.

What We want:
This competition is for Design only no coding! We need design for two pages.
We did some wireframing for the home page and the list of programs page. We made them just to show how we imagine the website would look like. But we encourage creative designs, so you don't have to stick to the wireframe models.

Sites We like:
http://www.ravenmoorcollege.example/
http://www.belvantis.example/fr/etudes.html
http://www.qtl.example/mba/Pages/default.aspx

Color schemes
The logo of the school is red and black. So the color scheme of the website should match that. For the rest, it is opened to your imagination.
Updates

The payment for the project is now garanteed. Good luck to you all !

Target Market(s)

The target market is diversified because we have students of different ages, also company representatives or employees that might visit the website for recruitment purposes. But the majority of our audience should be aged between 20 - 30 years.

Industry/Entity Type

Small Business

Requirements
Must have
• The design must include two pages: a home page and another interior page : might be the list of programs or any other page relevant to the domain. The Home page must include a slide show at the beginning.
The background page must be white.
Nice to have
• The use of flat design for this project is preferred.
The use of Pelican scaffold as a base for the design is an asset.

```html
<!DOCTYPE html>
<html lang="fr">
<head>
<meta charset="utf-8">
<title>KRVT – Ecole de management de projet</title>
<link href="https://fonts.googleapis.com/css2?family=Mako&family=Arimo:wght@400;700&display=swap" rel="stylesheet">
<style>
:root{
  --red:#d3080c;
  --red-dark:#a90407;
  --ink:#2b2b2b;
  --text:#444;
  --muted:#5b5b5b;
  --panel:#efefef;
  --line:#dcdcdc;
  --footer:#3b3b3b;
  --footer-text:#e6e6e6;
  --footer-head:#bdbdbd;
}
*{margin:0;padding:0;box-sizing:border-box}
html,body{width:1034px;height:1200px;overflow:hidden;background:#fff}
body{position:relative;font-family:"Arimo",Arial,sans-serif;color:var(--text)}
.abs{position:absolute}

/* top */
.topbar{left:0;top:0;width:1034px;height:36px;background:#f4f4f4;border-bottom:1px solid #d6d6d6}
.util-nav a{position:absolute;top:12px;font-family:"Mako",sans-serif;font-size:11px;color:#333;text-decoration:none;white-space:nowrap}
.util-nav a.active{color:var(--red)}
.hero{left:0;top:36px;width:1034px;height:320px;background:
  linear-gradient(180deg,rgba(255,255,255,.18) 0%,rgba(0,0,0,0) 40%,rgba(0,0,0,.12) 100%),
  linear-gradient(90deg,#8a706b 0%,#9b7f79 25%,#b08a78 38%,#c7a085 48%,#d8c3ab 62%,#c9b9a4 72%,#c5cad1 85%,#e6e8eb 100%)}
.brand{left:160px;top:34px;font-family:"Mako",sans-serif;font-size:26px;color:#1b1b1b;display:flex;align-items:center;gap:6px}
.brand i{display:block;width:14px;height:14px;background:var(--red)}
.main-nav{left:252px;top:0;width:174px;height:148px;background:var(--red)}
.main-nav .current{position:absolute;left:0;top:12px;width:174px;height:24px;background:var(--red-dark)}
.main-nav a{position:absolute;left:17px;font-family:"Mako",sans-serif;font-size:11.5px;color:#fff;text-decoration:none;white-space:nowrap}
.search{left:717px;top:37px;width:146px;height:28px;background:#f3f3f3;border:1px solid #d0d0d0;font-family:"Mako",sans-serif;font-size:13px;color:#666;padding:5px 0 0 13px}
.search-btn{left:863px;top:37px;width:31px;height:28px;background:#4a4a4a}
.slider-dots{left:205px;top:327px;width:120px;height:27px;background:#3a3a3a;display:flex;align-items:center;justify-content:center;gap:10px}
.slider-dots span{width:10px;height:10px;border-radius:50%;background:var(--red)}
.slider-dots span.on{background:#fff}

/* boxes */
.box-head{position:relative;background:var(--red);color:#fff;font-family:"Mako",sans-serif;font-size:17px;text-align:center;padding-top:9px;height:39px}
.box-head::before{content:"";position:absolute;left:50%;top:0;margin-left:-5px;border:5px solid transparent;border-top-color:#fff}
.side-list{background:var(--panel);list-style:none;padding-top:12px;height:165px}
.side-list li{position:relative;font-size:9.5px;color:#333;height:21.3px;padding-left:40px}
.side-list li::before{content:"›";position:absolute;left:18px;top:-4px;color:var(--red);font-weight:700;font-size:15px}
.video{background:var(--panel);font-family:"Mako",sans-serif;font-size:26px;color:#333;text-align:center;padding-top:35px;height:109px}
.more{font-size:10.5px;color:#222;font-weight:700;white-space:nowrap}
.more small{font-size:7px}

.intro h1{font-family:"Mako",sans-serif;font-weight:400;font-size:19px;color:#222}
.copy{font-size:9.5px;line-height:17.5px;color:var(--muted)}
.section-title{font-family:"Mako",sans-serif;font-size:19px;color:#222;font-weight:400}
.photo{background:linear-gradient(135deg,#e3ded6 0%,#c8bfb3 45%,#8f8273 100%)}
.photo.warm{background:linear-gradient(135deg,#c9584a 0%,#9a5447 45%,#4f3f3a 100%)}
.post-title{font-family:"Mako",sans-serif;font-size:13.5px;color:var(--red)}

.news-item .thumb{position:absolute;left:0;top:0;width:64px;height:58px;background:linear-gradient(180deg,#eef0f2 0%,#c9c2ba 35%,#8a7f76 62%,#2e4a7a 100%)}
.news-item p{position:absolute;left:77px;top:-2px;font-size:9px;line-height:16px;color:#444;white-space:nowrap}
.news-rule{height:1px;background:linear-gradient(90deg,#fff,#ddd,#fff)}

.divider{left:140px;top:816px;width:753px;height:1px;background:var(--line)}
.date{display:flex;align-items:center;gap:10px;font-family:"Mako",sans-serif;font-size:16px;color:#333}
.date b{background:var(--red);color:#fff;font-weight:400;padding:2px 5px;height:24px;width:42px}
.event-title{font-size:10.5px;color:var(--red)}
.partners{left:570px;top:840px;width:323px;height:134px;background:#efefef;border:1px solid #dedede}
.partner{position:absolute;width:62px;height:30px;background:#d2d2d2;border:1px solid #b8b8b8}

.share{left:989px;top:521px;width:45px;height:216px;background:#d9d9d9}
.share .btn{position:absolute;left:4px;width:37px;height:37px;background:#444}

/* footer */
.footer{left:0;top:1033px;width:1034px;height:167px;background:var(--footer)}
.footer h3{position:absolute;top:19px;font-family:"Mako",sans-serif;font-weight:400;font-size:15px;color:var(--footer-head)}
.footer ul{position:absolute;top:44px;list-style:none}
.footer li{font-size:9.5px;color:var(--footer-text);height:20.7px;white-space:nowrap}
.footer .txt{position:absolute;font-size:9.5px;line-height:13.5px;color:var(--footer-text)}
.social{position:absolute;top:47px;width:25px;height:25px;background:#777;border:2px solid #aaa}
.phone{position:absolute;left:584px;display:flex;align-items:center;gap:14px;font-size:11px;color:var(--footer-text)}
.nl-input{position:absolute;left:777px;top:102px;width:81px;height:23px;background:#2c2c2c}
.nl-send{position:absolute;left:858px;top:102px;width:35px;height:23px;background:#e9e9e9;font-size:9.5px;color:#333;text-align:center;padding-top:6px}
</style>
</head>
<body>

<header>
  <div class="abs topbar"></div>
  <div class="abs hero" role="img" aria-label="Photo d'étudiants travaillant devant un tableau blanc, bâtiment en brique en fond"></div>
  <nav class="util-nav">
    <a class="active" style="left:452px">Repertoire du personal</a>
    <a style="left:591px">Blogue</a>
    <a style="left:654px">Salle de presse</a>
    <a style="left:754px">Nous joindre</a>
    <a style="left:845px">Francais</a>
  </nav>
  <div class="abs brand"><i></i>KRVT</div>
  <nav class="abs main-nav">
    <span class="current"></span>
    <a style="top:18px">A propos de l'KRVT</a>
    <a style="top:45px">Programmes et Formations</a>
    <a style="top:69px">Etudiants</a>
    <a style="top:92px">Nouvelles et Evenements</a>
    <a style="top:116px">Entreprises</a>
  </nav>
  <div class="abs search">Search</div>
  <div class="abs search-btn">
    <svg width="31" height="28" viewBox="0 0 31 28"><circle cx="14" cy="12.5" r="5" fill="none" stroke="#ddd" stroke-width="1.6"/><line x1="17.6" y1="16" x2="21" y2="19.5" stroke="#ddd" stroke-width="1.8"/></svg>
  </div>
  <div class="abs slider-dots"><span class="on"></span><span></span><span></span><span></span><span></span></div>
</header>

<aside>
  <div class="abs" style="left:140px;top:382px;width:167px">
    <div class="box-head">Vousetes</div>
    <ul class="side-list">
      <li>Lorem ipsum dolor</li><li>Cum sociis natoque</li><li>Nullam ac euismod</li>
      <li>Proin posuere</li><li>Cras bibendum odio</li><li>Morbi rutrum varius</li><li>Vivamus vitae nunc</li>
    </ul>
  </div>
  <div class="abs" style="left:140px;top:615px;width:167px">
    <div class="box-head">KRVT.tv</div>
    <div class="video">Video</div>
  </div>
  <div class="abs more" style="left:141px;top:781px">View more <small>&gt;&gt;</small></div>
</aside>

<main>
  <section class="abs intro" style="left:339px;top:395px;width:360px">
    <h1>Lorem ipsum dolor sit amet, consectetur</h1>
    <p class="copy" style="margin-top:9px">Lorem ipsum dolor sit amet, consectetur adipiscing elit. Aliquam porttitor dui quis tincidunt feugiat. Nulla ante odio, pretium ut lectus sed, viverra fermentum nunc. Cum sociis natoque penatibus et magnis dis parturient montes, nascetur ridiculus mus. Aliquam erat volutpat...</p>
  </section>
  <h2 class="abs section-title" style="left:341px;top:516px">Blogue</h2>
  <article>
    <div class="abs photo" style="left:342px;top:557px;width:166px;height:119px" role="img" aria-label="Photo d'une salle de classe avec étudiants et enseignante"></div>
    <h3 class="abs post-title" style="left:343px;top:693px">Lorem ipsum</h3>
    <p class="abs copy" style="left:343px;top:716px;width:160px">Lorem ipsum dolor sit amet, con-sectetur adipiscing elit. Aliquam porttitor dui quis tincidunt feugiat.</p>
    <div class="abs more" style="left:343px;top:779px">Read more <small>&gt;&gt;</small></div>
  </article>
  <article>
    <div class="abs photo warm" style="left:526px;top:557px;width:165px;height:119px" role="img" aria-label="Photo de deux étudiants lisant ensemble"></div>
    <h3 class="abs post-title" style="left:527px;top:693px">Nullam ac euismod</h3>
    <p class="abs copy" style="left:527px;top:716px;width:160px">Proin posuere, velit non interdum volutpat, quam lacus auctor nulla, sed lobortis sem magna in nibh.</p>
    <div class="abs more" style="left:527px;top:779px">Read more <small>&gt;&gt;</small></div>
  </article>
</main>

<aside>
  <div class="abs" style="left:727px;top:382px;width:166px">
    <div class="box-head">Nouvelles</div>
  </div>
  <div class="abs news-item" style="left:728px;top:434px"><div class="thumb" role="img" aria-label="Portrait d'un intervenant"></div><p>Proin posuere, velit<br>Non interdum volu-<br>Pat, quam lacus<br>Auctor nulla, sed</p></div>
  <div class="abs news-rule" style="left:728px;top:507px;width:165px"></div>
  <div class="abs news-item" style="left:728px;top:525px"><div class="thumb" role="img" aria-label="Portrait d'un intervenant"></div><p>Proin posuere, velit<br>Non interdum volu-<br>Pat, quam lacus<br>Auctor nulla, sed</p></div>
  <div class="abs news-rule" style="left:728px;top:598px;width:165px"></div>
  <div class="abs news-item" style="left:728px;top:617px"><div class="thumb" role="img" aria-label="Portrait d'un intervenant"></div><p>Proin posuere, velit<br>Non interdum volu-<br>Pat, quam lacus<br>Auctor nulla, sed</p></div>
  <div class="abs news-rule" style="left:728px;top:690px;width:165px"></div>
  <div class="abs news-item" style="left:728px;top:708px"><div class="thumb" role="img" aria-label="Portrait d'un intervenant"></div><p>Proin posuere, velit<br>Non interdum volu-<br>Pat, quam lacus<br>Auctor nulla, sed</p></div>
  <div class="abs more" style="left:728px;top:781px">Read more <small>&gt;&gt;</small></div>
</aside>

<section>
  <div class="abs divider"></div>
  <h2 class="abs section-title" style="left:141px;top:832px">Events</h2>
  <div class="abs date" style="left:141px;top:870px"><b>Feb.</b>21</div>
  <p class="abs event-title" style="left:142px;top:909px">Lorem ipsum dolor sit amet,</p>
  <p class="abs copy" style="left:142px;top:926px;width:185px">Lorem ipsum dolor sit amet, consectetur adipiscing elit. Aliquam porttitor dui quis tincidunt feugiat.</p>
  <div class="abs more" style="left:141px;top:990px">Read more <small>&gt;&gt;</small></div>
  <div class="abs date" style="left:342px;top:870px"><b>Feb.</b>25</div>
  <p class="abs event-title" style="left:343px;top:909px">Lorem ipsum dolor sit amet,</p>
  <p class="abs copy" style="left:343px;top:926px;width:185px">Lorem ipsum dolor sit amet, consectetur adipiscing elit. Aliquam porttitor dui quis tincidunt feugiat.</p>

  <div class="abs partners" aria-label="Partenaires">
    <div class="partner" style="left:20px;top:19px"></div>
    <div class="partner" style="left:128px;top:19px"></div>
    <div class="partner" style="left:236px;top:19px"></div>
    <div class="partner" style="left:20px;top:76px"></div>
    <div class="partner" style="left:128px;top:76px"></div>
    <div class="partner" style="left:236px;top:76px"></div>
  </div>
</section>

<div class="abs share">
  <div class="btn" style="top:5px" aria-label="Partager"></div>
  <div class="btn" style="top:47px" aria-label="Partager"></div>
  <div class="btn" style="top:89px" aria-label="Partager"></div>
  <div class="btn" style="top:131px">
    <svg width="37" height="37" viewBox="0 0 37 37"><rect x="12" y="9" width="13" height="6" fill="#eee"/><rect x="8" y="15" width="21" height="9" rx="1" fill="#eee"/><rect x="12" y="21" width="13" height="7" fill="#fff" stroke="#444"/></svg>
  </div>
  <div class="btn" style="top:173px">
    <svg width="37" height="37" viewBox="0 0 37 37"><ellipse cx="17" cy="17" rx="10" ry="7" fill="#eee"/><path d="M11 21 L9 28 L16 23Z" fill="#eee"/><ellipse cx="22" cy="20" rx="7" ry="5" fill="none" stroke="#eee" stroke-width="1.4"/></svg>
  </div>
</div>

<footer class="abs footer">
  <h3 style="left:142px">Social</h3>
  <span class="social" style="left:143px" aria-label="Réseau social"></span>
  <span class="social" style="left:178px" aria-label="Réseau social"></span>
  <span class="social" style="left:211px" aria-label="Réseau social"></span>
  <span class="social" style="left:245px" aria-label="Réseau social"></span>

  <h3 style="left:318px">Link1</h3>
  <ul style="left:320px"><li>Lorem ipsum dolor</li><li>Cum sociis natoque</li><li>Nullam ac euismod</li><li>Proin posuere</li><li>Cras bibendum odio</li></ul>

  <h3 style="left:449px">Link2</h3>
  <ul style="left:451px"><li>Lorem ipsum dolor</li><li>Cum sociis natoque</li><li>Nullam ac euismod</li><li>Proin posuere</li><li>Cras bibendum odio</li></ul>

  <h3 style="left:584px">Contact Us</h3>
  <p class="txt" style="left:586px;top:45px;width:160px">Lorem ipsum dolor Cum sociis natoque Nullam ac euismod Proin posuere</p>
  <div class="phone" style="top:96px"><svg width="16" height="14" viewBox="0 0 16 14"><path d="M2 3 Q8 -1 14 3 L12 6 L10 4 Q8 3.5 6 4 L4 6Z" fill="#bbb"/><rect x="5" y="7" width="6" height="5" rx="1" fill="#bbb"/></svg>(000) 41 527 30 18</div>
  <div class="phone" style="top:122px"><svg width="16" height="14" viewBox="0 0 16 14"><path d="M2 3 Q8 -1 14 3 L12 6 L10 4 Q8 3.5 6 4 L4 6Z" fill="#bbb"/><rect x="5" y="7" width="6" height="5" rx="1" fill="#bbb"/></svg>(000) 62 904 17 43</div>

  <h3 style="left:775px">Newsletter</h3>
  <p class="txt" style="left:775px;top:45px;width:120px">Lorem ipsum dolor Cum sociis natoque Nullam ac euismod Proin posuere</p>
  <div class="nl-input"></div>
  <div class="nl-send">Send</div>
</footer>

</body>
</html>
```